I need a brochure for an Outdoor Umbrella Company

Please see the below referenced website for the requirements

http://brightcanopyshade.example-sites.com

I need a brochure design for startup company based in Los Angeles called gorvalshades Inc. This is for an outdoor umbrella that has prongs that makes it uniquely capable of sticking it into the ground for outdoor activities. I would like to see colors that complement the color of the photographs that are attached. The final draft should communicate the positives that are highlighted on the website and the fact that this is the only umbrella in the world that seats into the ground very easily.

```html
<!DOCTYPE html>
<html lang="en">
<head>
<meta charset="utf-8">
<title>TerraStake Umbrella Brochure</title>
<link rel="stylesheet" href="https://fonts.googleapis.com/css2?family=Lora:wght@400;500&family=Merriweather:wght@300;400&family=Arimo:wght@700&display=swap">
<style>
  :root {
    --brand-red: #b52d2a;
    --heading-red: #a8322d;
    --brand-gold: #f1c35a;
    --cream: #faf2dc;
    --body-text: #3f3f3f;
    --phone-blue: #2a6fb6;
    --umbrella-red: #e5403f;
    --umbrella-blue: #2a5db4;
    --divider: #c9c9c9;
    --white: #ffffff;
  }
  * { box-sizing: border-box; margin: 0; padding: 0; }
  html, body { width: 1200px; height: 927px; overflow: hidden; background: var(--white); }
  .brochure { position: relative; width: 1200px; height: 927px; background: var(--white); font-family: "Merriweather", Georgia, serif; color: var(--body-text); }
  .fold-line { position: absolute; top: 0; bottom: 0; border-left: 1px dashed var(--divider); }
  .fold-line--one { left: 406px; }
  .fold-line--two { left: 811px; }

  .panel { position: absolute; top: 0; height: 927px; }
  .panel--left { left: 55px; width: 294px; }
  .panel--middle { left: 463px; width: 296px; }
  .panel--right { left: 870px; width: 285px; }

  .top-bar { position: absolute; top: 55px; left: 0; width: 100%; height: 21px; }
  .top-bar--red { background: var(--brand-red); }
  .top-bar--gold { background: var(--brand-gold); }

  .photo { position: absolute; }
  .photo--blue-umbrella { top: 88px; left: 14px; width: 266px; height: 292px; background: linear-gradient(180deg, #dfe6f4 0%, #eef2f8 45%, #ffffff 100%); }

  .section-title { position: absolute; font-family: "Lora", Georgia, serif; font-weight: 400; color: var(--heading-red); }
  .panel--left .section-title { top: 402px; left: 11px; font-size: 30px; }

  .features { position: absolute; top: 470px; left: 11px; width: 264px; font-size: 12px; line-height: 16px; font-weight: 300; }
  .features__label { text-transform: uppercase; margin-bottom: 11px; letter-spacing: .3px; }
  .features__list { list-style: none; }
  .features__list li { position: relative; padding-left: 22px; margin-bottom: 9px; }
  .features__list li::before { content: "•"; position: absolute; left: 2px; top: 0; }
  .features__offer { margin-top: 28px; }

  .call-label { position: absolute; font-family: "Arimo", Arial, sans-serif; font-weight: 700; }
  .panel--left .call-label { top: 800px; left: 11px; font-size: 16px; color: #4d4d4d; }

  .footer-box { position: absolute; top: 825px; left: 0; width: 100%; height: 56px; display: flex; align-items: center; justify-content: center; }
  .footer-box--red { background: var(--brand-red); color: var(--white); }
  .footer-box--gold { background: var(--brand-gold); color: #222; }
  .footer-box__phone { font-family: "Lora", Georgia, serif; font-size: 28px; }
  .footer-box__email, .footer-box__web { font-family: "Lora", Georgia, serif; font-size: 17px; }

  .photo--red-umbrella { top: 83px; left: 0; width: 296px; height: 307px; background: linear-gradient(180deg, #f6dcd0 0%, var(--cream) 40%, var(--cream) 100%); }
  .photo--carry-bag { top: 391px; left: 0; width: 296px; height: 44px; background: #e0403c; }
  .photo--canopy-top { top: 468px; left: 0; width: 296px; height: 330px; background: linear-gradient(180deg, #e84a45 0%, #e23c3a 100%); }
  .email-label { position: absolute; top: 798px; left: 0; width: 100%; text-align: center; font-family: "Lora", Georgia, serif; font-size: 19px; color: #111; }

  .panel--right .section-title { top: 106px; left: 0; width: 100%; text-align: center; font-size: 20px; line-height: 1.5; }
  .copy { position: absolute; top: 200px; left: 12px; width: 263px; font-size: 14.5px; line-height: 1.35; font-weight: 300; text-align: justify; }
  .copy p { margin-bottom: 13px; }
  .copy .copy__tagline { margin-top: 40px; text-align: left; }
  .panel--right .call-label { top: 655px; left: 0; width: 100%; text-align: center; font-size: 20px; color: #111; }
  .phone-number { position: absolute; top: 680px; left: 0; width: 100%; text-align: center; font-family: "Lora", Georgia, serif; font-size: 34px; color: var(--phone-blue); }
</style>
</head>
<body>
<main class="brochure">
  <div class="fold-line fold-line--one"></div>
  <div class="fold-line fold-line--two"></div>

  <section class="panel panel--left">
    <div class="top-bar top-bar--red"></div>
    <div class="photo photo--blue-umbrella" role="img" aria-label="Photo: blue outdoor umbrella staked in the ground beside its carry bag"></div>
    <h2 class="section-title">About our Product</h2>
    <div class="features">
      <p class="features__label">Features</p>
      <ul class="features__list">
        <li>Fade Resistant Cover</li>
        <li>Stainless Steel</li>
        <li>Water Resistant Cover</li>
        <li>Sharp prongs anchors that slide very easily into turf or ground</li>
        <li>Telescopic nipples on shaft to adjust the height</li>
        <li>This umbrella collapses down easily after use, which makes it very portable.</li>
      </ul>
      <p class="features__offer">If you order today, you will also receive a protective cover that fits over the sharp anchor points!</p>
    </div>
    <p class="call-label">CALL US NOW!</p>
    <div class="footer-box footer-box--red"><span class="footer-box__phone">555.014.2290</span></div>
  </section>

  <section class="panel panel--middle">
    <div class="top-bar top-bar--gold"></div>
    <div class="photo photo--red-umbrella" role="img" aria-label="Photo: red outdoor umbrella with ground prongs and a quality seal"></div>
    <div class="photo photo--carry-bag" role="img" aria-label="Photo: red carry bag for the umbrella"></div>
    <div class="photo photo--canopy-top" role="img" aria-label="Photo: red umbrella canopy seen from above"></div>
    <p class="email-label">E-mail</p>
    <div class="footer-box footer-box--gold"><span class="footer-box__email">hello@brightcanopyshade.com</span></div>
  </section>

  <section class="panel panel--right">
    <div class="top-bar top-bar--red"></div>
    <h2 class="section-title">What Makes the TerraStake<br>Umbrella the Right Choice?</h2>
    <div class="copy">
      <p>Unlike other outdoor umbrellas, the TerraStake anchors into the ground very firmly and easily.</p>
      <p>The TerraStake umbrella is great for outdoor activities like sports, fishing and hunting. Everytime you go outdoors, the TerraStake will be there for your convenience!</p>
      <p>No matter what surface you are on, the TerraStake will easily plant itself into the ground. This umbrella works extremely well on grassy fields and different types of turf, regardless of of how dry, wet, hard, or soft the conditions are.</p>
      <p class="copy__tagline">Just step and then relax!</p>
    </div>
    <p class="call-label">CALL US NOW!</p>
    <p class="phone-number">555.014.2290</p>
    <div class="footer-box footer-box--red"><span class="footer-box__web">www.brightcanopyshade.com</span></div>
  </section>
</main>
</body>
</html>
```